Varnoth Immigration _Cloud-based, boutique law firm serving clients worldwide in US Immigration Law

I need a website for my new US immigration law firm that will be based in Montreal, QC Canada but serve clients worldwide to achieve their US immigration goals. This will be a boutique firm offering attentive and compassionate service to our corporate and individual clients. I'd like the site to be fresh, modern, sophisticated and easy to read.

I will need a home page, about/bio page, services page, and contact me page with a form so potential clients could email inquiries and also schedule consultations. I would also like a 'Book a Consultation' button on the home page (easily visible).

The longest website page is going to be the 'Services' tab, which I'd like to break down to services for Employers and services Individuals, with further sub-sets of services to each type of client. I envision images with short text that display longer text when hoovering over.

To start, I would have 3 subsets of services for Employers and 5 subsets of services for Individuals. I will need the ability to expand/edit these pages in Wix interface as we grow.

The site will need to be in English and in French.

I like the color blue and the final design should communicate the firm's core values: integrity and compassion. In other words, we do right, no matter what and are understanding to individual circumstances. I'd like the site to convey sophistication and accessibility. I don't like staged stock photos of people. Sites with a lot of stock photos of people feels unauthentic to me.

Logo draft is attached in jpeg. Navy and gold colors.
Example of 4 law firm sites I like below:
- https://www.quellanlawzpt.com/
-https://www.tvbrelaw.com/
-https://kemblinappeals.com/
-https://www.orundalaw.com/

Target Market(s)

Small-medium sized businesses (10-999 employees) in US with foreign workforce; Foreign entrepreneurs wishing to implant in the US

Industry/Entity Type

Law

Coding

Coded - Design and coding required

Font styles to use
Sans Serif

Colors

Designer to choose colors to be used in the design.

Requirements
Must have
• Great Home Page (Grabs attention with eye-catching images/text; Immediately establishes credibility; Provides an overview of services; Encourages visitor to take the next action.)
Nice to have
• Images of Montreal (where firm is based); Images of bridges (symbolizes progress, movement, connections)
Should not have
• Non-authentic photos: staged people at desks or pictures of court buildings.

```html
<!DOCTYPE html>
<html lang="en">
<head>
<meta charset="utf-8">
<title>Varnoth Immigration</title>
<link href="https://fonts.googleapis.com/css2?family=Libre+Baskerville&family=Roboto:wght@400;500;700&display=swap" rel="stylesheet">
<style>
:root{
  --navy:#323b56;
  --navy-dark:#283049;
  --gold:#b6944f;
  --gold-soft:#c4a566;
  --white:#ffffff;
  --text:#555a66;
  --muted:#8a8f99;
  --line:#d9dbe0;
}
*{margin:0;padding:0;box-sizing:border-box}
html,body{width:1200px;height:3231px;overflow:hidden}
body{position:relative;background:var(--white);font-family:'Roboto',sans-serif;color:var(--text)}
.abs{position:absolute}

/* header */
.site-header{position:absolute;left:0;top:0;width:1200px;height:102px;background:var(--navy)}
.brand{position:absolute;display:flex;align-items:center;gap:10px;color:var(--gold-soft)}
.brand-mark{width:44px;height:44px;border-radius:50%;background:#6d6a5e;flex:none}
.brand-name{font-family:'Libre Baskerville',serif;font-size:17px;line-height:19px;letter-spacing:2px}
.brand-sub{font-family:'Libre Baskerville',serif;font-size:6.5px;letter-spacing:1.5px;margin-top:3px}
.main-nav{position:absolute;left:378px;top:0;height:102px;display:flex}
.main-nav a{display:flex;align-items:center;padding:0 20px;height:102px;color:var(--white);font-size:14px;font-weight:500;text-decoration:none;border-right:1px solid #444d68}
.main-nav a.active{background:var(--gold)}
.caret{display:inline-block;width:6px;height:6px;border-right:1.5px solid #fff;border-bottom:1.5px solid #fff;transform:rotate(45deg);margin:-4px 0 0 8px}
.social{position:absolute;display:flex;gap:4px}
.social span{width:32px;height:32px;border-radius:50%;border:1px solid #fff}
.social span.on{background:var(--gold);border-color:var(--gold)}
.lang{position:absolute;left:1044px;top:42px;color:#fff;font-size:14px;font-weight:500}

/* hero */
.hero{position:absolute;left:0;top:102px;width:1200px;height:1181px;background:var(--navy)}
.hero-box{position:absolute;left:326px;top:176px;width:548px;height:229px;background:rgba(255,255,255,.45);text-align:center}
.hero-box h1{font-family:'Libre Baskerville',serif;font-weight:400;font-size:33px;color:var(--navy);margin-top:28px}
.hero-box p{font-size:15.5px;line-height:26px;color:#2d3345;margin:8px 50px 0}
.btn{display:inline-block;background:var(--gold);color:#fff;font-size:13px;font-weight:500;text-transform:uppercase}
.hero-box .btn{margin-top:16px;padding:14px 19px}
.dots{position:absolute;left:566px;top:544px;display:flex;gap:7px}
.dots i{width:12px;height:12px;border-radius:50%;border:1.5px solid #fff}
.dots i.on{background:#fff}

/* about */
.about-title{position:absolute;left:598px;top:800px;font-family:'Libre Baskerville',serif;font-size:37px;color:#fff;font-weight:400}
.about-text{position:absolute;left:598px;top:868px;width:452px;color:#fff;font-size:14.5px;line-height:25.6px;text-align:justify}
.about-text p+p{margin-top:10px}
.about-btn{position:absolute;left:598px;top:1117px;width:137px;height:44px;line-height:44px;text-align:center}

/* services */
.section-title{position:absolute;left:0;width:1200px;text-align:center;font-family:'Libre Baskerville',serif;font-weight:400;font-size:40px}
.service-card{position:absolute;top:1463px;width:228px;height:286px;background:#fff;box-shadow:0 2px 12px rgba(0,0,0,.12);text-align:center}
.service-card.current{border:2px solid var(--gold);box-shadow:none}
.service-icon{width:86px;height:86px;border-radius:50%;background:var(--navy);margin:29px auto 0;display:flex;align-items:center;justify-content:center}
.current .service-icon{background:var(--gold)}
.service-card h3{font-size:16px;font-weight:500;color:var(--gold);margin-top:29px}
.current h3{color:var(--navy)}
.service-card p{font-size:12.5px;line-height:21.5px;color:#666;margin:10px 8px 0}

/* testimonials */
.testimonials{position:absolute;left:0;top:1853px;width:1200px;height:446px;background:linear-gradient(180deg,#b69651 0%,#a98a48 50%,#b29350 100%)}
.testimonial{position:absolute;top:158px;width:407px;height:213px;background:#fff;border-radius:34px}
.avatar-ring{position:absolute;left:-55px;top:48px;width:112px;height:112px;border-radius:50%;border:2px solid #fff;display:flex;align-items:center;justify-content:center}
.avatar{width:94px;height:94px;border-radius:50%;background:linear-gradient(135deg,#8a8f96,#c9c3bb)}
.quote{position:absolute;left:80px;top:10px;font-family:'Libre Baskerville',serif;font-size:60px;color:var(--gold);line-height:1}
.testimonial p{position:absolute;left:80px;top:68px;width:300px;font-size:12.5px;line-height:21px;color:#666;text-align:justify}
.testimonial h4{position:absolute;left:80px;top:152px;font-size:16px;font-weight:500;color:var(--navy)}
.stars{position:absolute;left:80px;top:175px;color:#f2a81d;font-size:10px;letter-spacing:1px}

/* contact */
.contact-photo{position:absolute;left:109px;top:2409px;width:447px;height:384px;background:linear-gradient(160deg,#3a4560,#263049)}
.contact-kicker{position:absolute;right:782px;top:2512px;font-family:'Libre Baskerville',serif;font-size:18px;color:#fff}
.contact-head{position:absolute;right:782px;top:2548px;text-align:right;font-size:38px;line-height:53px;font-weight:700;color:#fff}
.gold-frame{position:absolute;left:742px;top:2429px;width:366px;height:346px;border:4px solid var(--gold)}
.form-card{position:absolute;left:462px;top:2460px;width:625px;height:432px;background:#fff;box-shadow:0 3px 18px rgba(0,0,0,.12)}
.form-card h2{position:absolute;left:52px;top:50px;font-family:'Libre Baskerville',serif;font-weight:400;font-size:20px;color:var(--navy)}
.field{position:absolute;width:230px;border-bottom:1px solid var(--line);height:60px}
.field label{display:block;font-size:14.5px;color:#333;font-weight:500}
.field span{display:block;font-size:12.5px;color:var(--muted);margin-top:12px;padding-left:2px}
.send{position:absolute;left:501px;top:325px;width:64px;height:64px;border-radius:50%;background:var(--gold);display:flex;align-items:center;justify-content:center}
.dot-grid{position:absolute;left:76px;top:2693px;width:146px;height:148px;background-image:radial-gradient(circle,#c5c8d0 1.2px,transparent 1.5px);background-size:12px 12px}

/* footer */
.site-footer{position:absolute;left:0;top:3005px;width:1200px;height:226px;background:var(--navy)}
.footer-nav{position:absolute;right:112px;top:60px;display:flex;color:#fff;font-size:14px;font-weight:500}
.footer-nav span{padding:0 4px}
.footer-nav b{font-weight:400;padding:0 18px}
.footer-rule{position:absolute;left:112px;top:158px;width:976px;height:1px;background:#4a526b}
.copyright{position:absolute;left:0;width:1200px;top:182px;text-align:center;color:#fff;font-size:13px}
</style>
</head>
<body>

<section class="hero">
  <svg class="abs" style="left:0;top:0" width="1200" height="620" viewBox="0 0 1200 620">
    <defs>
      <linearGradient id="sky" x1="0" y1="0" x2="0" y2="1">
        <stop offset="0" stop-color="#3f7fd0"/>
        <stop offset=".35" stop-color="#a9c7e6"/>
        <stop offset=".55" stop-color="#7f9a6a"/>
        <stop offset=".8" stop-color="#5d6a4e"/>
        <stop offset="1" stop-color="#8c9aa3"/>
      </linearGradient>
    </defs>
    <path d="M0 426 Q600 778 1200 426 L1200 0 L0 0Z" fill="#fff"/>
    <path role="img" aria-label="Montreal old port waterfront with skyline and domed market building" d="M0 426 Q600 734 1200 426 L1200 0 L0 0Z" fill="url(#sky)"/>
  </svg>
  <div class="hero-box">
    <h1>VARNOTH IMMIGRATION</h1>
    <p>Lorem ipsum dolor sit amet consectetur adipiscing elit sed do eius sedmod tempor incididunt laborea.</p>
    <span class="btn">Book a consultation</span>
  </div>
  <div class="dots"><i></i><i class="on"></i><i></i><i></i></div>
</section>

<header class="site-header">
  <div class="brand" style="left:112px;top:28px">
    <span class="brand-mark"></span>
    <div><div class="brand-name">VARNOTH<br>IMMIGRATION</div><div class="brand-sub">MAREN VARNOTH, ATTORNEY</div></div>
  </div>
  <nav class="main-nav">
    <a class="active">HOME</a><a>ABOUT ME</a><a>SERVICES<span class="caret"></span></a><a>CONTACT ME</a>
  </nav>
  <div class="social" style="left:868px;top:35px"><span class="on"></span><span></span><span></span><span></span></div>
  <div class="lang">ENG<span class="caret"></span></div>
</header>

<svg class="abs" style="left:111px;top:745px" width="426" height="452">
  <circle cx="213" cy="238" r="213" fill="#b6944f"/>
  <circle role="img" aria-label="Portrait of the attorney" cx="213" cy="223" r="197" fill="#d6d7d9"/>
</svg>
<h2 class="about-title">ABOUT ME</h2>
<div class="about-text">
  <p>Lorem ipsum dolor sit amet, consectetur adipiscing elit, sed do eiusmod tempor incididunt ut labore et dolore magna aliqua. Ut enim ad minim veniam, quis nostrud exercitation ullamco laboris nisi ut aliquip ex ea commodo consequat duis aute irure dolor in repreh enderit in voluptate velit esse cillum dolorea.</p>
  <p>Lorem ipsum dolor sit amet, consectetur adipiscing elit, sed do eiusmod tempor incididunt ut labore et dolore magna aliqua. Ut enim ad minim veniam quis nostrud exercita.</p>
</div>
<span class="btn about-btn">Learn more</span>

<h2 class="section-title" style="top:1374px;color:var(--navy)">SERVICES</h2>
<div class="service-card" style="left:112px">
  <div class="service-icon"><svg width="44" height="44" fill="none" stroke="#fff" stroke-width="1.6"><circle cx="20" cy="20" r="13"/><ellipse cx="20" cy="20" rx="6" ry="13"/><path d="M7 20h26M9 13h22M9 27h22"/><circle cx="36" cy="34" r="3"/></svg></div>
  <h3>LORUM IPSUM DOL</h3>
  <p>Lorem ipsum dolor sit amet consec tetur adipiscing elit, sed do eiu smod tempor incididunt ut labore et dolore magna aliqua.</p>
</div>
<div class="service-card" style="left:361px">
  <div class="service-icon"><svg width="44" height="44" fill="none" stroke="#fff" stroke-width="1.6"><circle cx="22" cy="14" r="6"/><path d="M12 30c3-8 17-8 20 0"/><path d="M4 28l8 8h20l8-8"/></svg></div>
  <h3>LORUM IPSUM DOL</h3>
  <p>Lorem ipsum dolor sit amet consec tetur adipiscing elit, sed do eiu smod tempor incididunt ut labore et dolore magna aliqua.</p>
</div>
<div class="service-card current" style="left:611px">
  <div class="service-icon"><svg width="44" height="44" fill="none" stroke="#fff" stroke-width="1.6"><rect x="9" y="5" width="22" height="30" rx="2"/><path d="M14 13h12M14 19h12M14 25h7"/><circle cx="32" cy="32" r="7"/><path d="M29 32l2 2 4-4"/></svg></div>
  <h3>LORUM IPSUM DOL</h3>
  <p>Lorem ipsum dolor sit amet consec tetur adipiscing elit, sed do eiu smod tempor incididunt ut labore et dolore magna aliqua.</p>
</div>
<div class="service-card" style="left:861px">
  <div class="service-icon"><svg width="44" height="44" fill="none" stroke="#fff" stroke-width="1.6"><circle cx="22" cy="12" r="5"/><circle cx="10" cy="20" r="4"/><circle cx="34" cy="20" r="4"/><path d="M14 36c1-8 15-8 16 0M3 32c1-5 11-5 12 0M29 32c1-5 11-5 12 0"/></svg></div>
  <h3>LORUM IPSUM DOL</h3>
  <p>Lorem ipsum dolor sit amet consec tetur adipiscing elit, sed do eiu smod tempor incididunt ut labore et dolore magna aliqua.</p>
</div>

<section class="testimonials" role="img" aria-label="Aerial view of a bridge over a river in autumn, gold tinted">
  <h2 class="section-title" style="top:67px;color:#fff">TESTIMONIALS</h2>
  <div class="testimonial" style="left:183px">
    <div class="avatar-ring"><div class="avatar" role="img" aria-label="Client portrait"></div></div>
    <div class="quote">“</div>
    <p>At vero eos et accusamus et iusto odio dignissimos ducimus qui blanditiis praesentium voluptatum deleniti atque corrupti quos dolores et quas.</p>
    <h4>JOHN SMITH</h4>
    <div class="stars">★★★★★</div>
  </div>
  <div class="testimonial" style="left:663px">
    <div class="avatar-ring"><div class="avatar" role="img" aria-label="Client portrait"></div></div>
    <div class="quote">“</div>
    <p>At vero eos et accusamus et iusto odio dignissimos ducimus qui blanditiis praesentium voluptatum deleniti atque corrupti quos dolores et quas.</p>
    <h4>JOHN SMITH</h4>
    <div class="stars">★★★★★</div>
  </div>
</section>

<div class="dot-grid"></div>
<div class="contact-photo" role="img" aria-label="Dim navy toned office interior"></div>
<div class="contact-kicker">CONTACT US</div>
<div class="contact-head">LET’S DO<br>GOOD<br>TOGETHER!</div>
<div class="gold-frame"></div>
<form class="form-card">
  <h2>SEND US A MESSAGE</h2>
  <div class="field" style="left:56px;top:108px"><label>First Name</label><span>John</span></div>
  <div class="field" style="left:332px;top:108px"><label>Last Name</label><span>Smith</span></div>
  <div class="field" style="left:56px;top:201px"><label>Email Address</label><span>johnsmith@inboxly.com</span></div>
  <div class="field" style="left:332px;top:201px"><label>Phone</label><span>+1 (888) 888 8888</span></div>
  <div class="field" style="left:56px;top:294px;width:452px;height:86px"><label>Message</label><span>Lorem ipsum dolor sit a tetur adipiscing...|</span></div>
  <div class="send"><svg width="26" height="26" viewBox="0 0 26 26"><path d="M24 2L2 12l8 3 3 9z" fill="#fff"/><path d="M24 2L10 15" stroke="#b6944f" stroke-width="1.5"/></svg></div>
</form>

<footer class="site-footer">
  <div class="brand" style="left:112px;top:64px">
    <span class="brand-mark" style="width:60px;height:60px"></span>
    <div><div class="brand-name" style="font-size:20px;line-height:25px">VARNOTH<br>IMMIGRATION</div><div class="brand-sub" style="font-size:8px">MAREN VARNOTH, ATTORNEY</div></div>
  </div>
  <div class="footer-nav"><span>HOME</span><b>|</b><span>ABOUT ME</span><b>|</b><span>SERVICES</span><b>|</b><span>CONTACT ME</span></div>
  <div class="social" style="left:948px;top:97px"><span class="on"></span><span></span><span></span><span></span></div>
  <div class="footer-rule"></div>
  <div class="copyright">© 2023 <b style="font-weight:500">VARNOTH IMMIGRATION</b> &nbsp; / &nbsp; All rights reserved.</div>
</footer>

</body>
</html>
```